Marcelo Vantrini
Tenor & Vocal Coach
mvbaritono@quellmail.net
(713) 562-8307
www.voicefromthecore.net
Want two sided postcard / rack card.4" x 9"
Front - vertical - picture in t-shirt, name, title (Tenor & Vocal Coach), contact information
Back - horizontal - picture in jacket, name, title (Tenor & Vocal Coach), contact information, bio (see attachment for words)
Do not leave space for an address.
Looking for an edgy modern design!

Target Market(s)

Young adults

Requirements
Nice to have
• Will pay extra to get a complimentary business card design, two sided

```html
<!DOCTYPE html>
<html lang="en">
<head>
<meta charset="UTF-8">
<title>Marcelo Vantrini – Rack Card</title>
<link href="https://fonts.googleapis.com/css2?family=Jost:wght@300;400&display=swap" rel="stylesheet">
<style>
  :root {
    --backdrop: #6f6f6f;
    --card: #353535;
    --ink: #ffffff;
    --wall-light: #ece8dc;
    --wall-mid: #c8c0cc;
    --shirt-grey: #9a98a8;
    --denim: #3c4a78;
    --blazer: #2c3452;
  }
  * { margin: 0; padding: 0; box-sizing: border-box; }
  html, body {
    width: 1200px; height: 1200px; overflow: hidden;
    background: var(--backdrop);
    font-family: "Jost", "Futura", sans-serif;
    color: var(--ink);
  }
  .stage { position: relative; width: 1200px; height: 1200px; }

  .name { font-weight: 400; letter-spacing: -0.5px; line-height: 1; white-space: nowrap; }
  .title { font-weight: 300; text-transform: uppercase; white-space: nowrap; line-height: 1.1; }
  .contact { font-weight: 300; white-space: nowrap; }
  .email { text-transform: uppercase; }

  /* Front – vertical */
  .card-front {
    position: absolute; left: 78px; top: 121px;
    width: 400px; height: 900px;
    background: var(--card);
  }
  .card-front .photo {
    position: absolute; left: 0; top: 0; width: 400px; height: 751px;
    background: linear-gradient(172deg, var(--wall-light) 0%, var(--wall-mid) 30%, var(--shirt-grey) 55%, #7c7f9a 80%, var(--denim) 100%);
  }
  .card-front .identity {
    position: absolute; right: 20px; top: 766px; text-align: right;
  }
  .card-front .name { font-size: 41px; }
  .card-front .title { font-size: 18.5px; margin-top: 6px; }
  .card-front .contact { font-size: 15px; line-height: 18px; margin-top: 12px; }

  /* Back – horizontal */
  .card-back {
    position: absolute; left: 270px; top: 367px;
    width: 900px; height: 400px;
    background: var(--card);
  }
  .card-back .text-column {
    position: absolute; left: 34px; top: 38px; width: 516px; text-align: right;
  }
  .card-back .name { font-size: 39px; }
  .card-back .title { font-size: 17px; margin-top: 5px; }
  .bio {
    text-align: left; font-size: 12px; font-weight: 300; line-height: 16.7px;
    margin-top: 42px;
  }
  .call-to-action { font-size: 24px; font-weight: 300; margin-top: 18px; white-space: nowrap; }
  .card-back .contact { font-size: 16px; line-height: 22px; margin-top: 12px; }
  .card-back .photo {
    position: absolute; left: 568px; top: 26px; width: 313px; height: 351px;
    background: radial-gradient(ellipse at 50% 35%, var(--wall-light) 0%, #d6cdb6 40%, #6e7090 75%, var(--blazer) 100%);
  }
</style>
</head>
<body>
<main class="stage">
  <section class="card-front">
    <div class="photo" role="img" aria-label="Portrait photo of the singer smiling, wearing a grey t-shirt and jeans, leaning against a pale wall"></div>
    <div class="identity">
      <h1 class="name">MARCELO VANTRINI</h1>
      <p class="title">Tenor &amp; Vocal Coach</p>
      <p class="contact"><span class="email">mvbaritono@quellmail.net</span><br>(713) 562-8307</p>
    </div>
  </section>

  <section class="card-back">
    <div class="text-column">
      <h2 class="name">MARCELO VANTRINI</h2>
      <p class="title">Tenor &amp; Vocal Coach</p>
      <p class="bio">
        Marcelo is a local singer and actor who has been working professionally around the country as a concert artist and musical theater performer.<br>
        He studied at the Ashgrove School of Music, Bayline University and works as a vocal coach with local youths and adults in Houston area.<br>
        Marcelo’s goal is to help his students master their individual instrument so that they can achieve a natural and effortless vocal production.
      </p>
      <p class="call-to-action">For more information please contact Marcelo today!</p>
      <p class="contact"><span class="email">mvbaritono@quellmail.net</span><br>(713) 562-8307</p>
    </div>
    <div class="photo" role="img" aria-label="Portrait photo of the singer in a dark blazer and white open-collar shirt against a pale wall"></div>
  </section>
</main>
</body>
</html>
```